Billboard design 8x3M LUMA (Spanish company)

We´re located in the south of Spain. We run a local telecom company.
We sell Fiber optic, and mobile phone lines mainly.
The billboard will have to be in Spanish, I would like the price to be something you spot on first sight when passing by in the car.
Our company color is blue, like in our logo which I will add. I will also add a example from what we currently have.
The new offer should be:
1000 megas + 100Gigas movil con llamadas ilimitadas. (meaning 1000Mb fiber optic speed and 100Gb data and unlimited calls for 1 mobile line)
Our details are: phone line 555 01 2345
Website: luma.example

```html
<!DOCTYPE html>
<html lang="es">
<head>
<meta charset="utf-8">
<title>LUMA – Valla 8x3</title>
<link href="https://fonts.googleapis.com/css2?family=Outfit:wght@600;700;800&display=swap" rel="stylesheet">
<style>
  :root {
    --page-bg: #e9edf1;
    --blue-deep: #0a4a73;
    --blue-mid: #0f7fbf;
    --blue-light: #2fb2ec;
    --blue-ring: #0b5d8f;
    --orange: #ff9500;
    --white: #ffffff;
    --text-navy: #0e4a78;
    --art-orange: #f5811f;
    --art-dark: #3a1f12;
  }
  * { margin: 0; padding: 0; box-sizing: border-box; }
  html, body {
    width: 1200px; height: 874px; overflow: hidden;
    background: var(--page-bg);
    font-family: "Outfit", sans-serif;
  }
  .billboard {
    position: absolute; left: 0; top: 225px;
    width: 1200px; height: 424px;
    overflow: hidden;
    box-shadow: 0 10px 30px rgba(0,0,0,.18);
  }
  .offer-panel {
    position: absolute; left: 0; top: 0;
    width: 1200px; height: 340px;
    background: linear-gradient(90deg, var(--blue-deep) 25%, var(--blue-mid) 60%, var(--blue-light) 100%);
  }
  .price-shape { position: absolute; left: 0; top: 0; width: 400px; height: 340px; }
  .price {
    position: absolute; left: 14px; top: 66px;
    width: 290px; text-align: center; color: var(--white);
  }
  .price-amount { font-size: 124px; font-weight: 800; line-height: 1; letter-spacing: -1px; }
  .price-label { font-size: 36px; font-weight: 700; line-height: 1; margin-top: 4px; }
  .brand {
    position: absolute; left: 370px; top: 28px; width: 400px;
    text-align: center; color: var(--white);
  }
  .brand-name { font-size: 104px; font-weight: 800; line-height: 1; letter-spacing: 6px; }
  .brand-services { font-size: 28px; font-weight: 600; margin-top: 8px; white-space: nowrap; }
  .contact {
    position: absolute; left: 360px; top: 190px; width: 420px;
    color: var(--white); text-align: center;
  }
  .contact-web { font-size: 22px; font-weight: 700; letter-spacing: 8px; padding-left: 40px; white-space: nowrap; }
  .contact-phone {
    display: flex; align-items: center; justify-content: center; gap: 10px;
    font-size: 56px; font-weight: 800; line-height: 1; margin-top: 4px; white-space: nowrap;
  }
  .phone-icon { width: 40px; height: 40px; flex: none; }
  .hero-art {
    position: absolute; left: 800px; top: 10px; width: 375px; height: 310px;
    background:
      radial-gradient(circle at 60% 62%, var(--art-orange) 0 38%, transparent 60%),
      linear-gradient(135deg, rgba(255,255,255,0) 0 30%, var(--art-dark) 100%);
    border-radius: 40px 10px 10px 40px;
  }
  .headline-band {
    position: absolute; left: 0; top: 340px; width: 1200px; height: 84px;
    background: var(--white);
    display: flex; align-items: center; padding-left: 26px;
    color: var(--text-navy); white-space: nowrap;
  }
  .headline-main { font-size: 50px; font-weight: 800; letter-spacing: -.5px; }
  .headline-sub { font-size: 31px; font-weight: 800; margin-left: 14px; padding-top: 8px; }
</style>
</head>
<body>
  <div class="billboard">
    <div class="offer-panel">
      <svg class="price-shape" viewBox="0 0 400 340" aria-hidden="true">
        <path d="M0 0 H252 C360 95 350 245 312 340 H0 Z" fill="var(--blue-ring)"/>
        <path d="M0 0 H228 C330 95 320 245 287 340 H0 Z" fill="var(--orange)"/>
      </svg>
      <div class="price">
        <div class="price-amount">35€</div>
        <div class="price-label">Por sólo</div>
      </div>
      <div class="brand">
        <div class="brand-name">LUMA</div>
        <div class="brand-services">Wifi | Fibra | Movil | Tv</div>
      </div>
      <div class="contact">
        <div class="contact-web">www.luma.example</div>
        <div class="contact-phone">
          <svg class="phone-icon" viewBox="0 0 40 40" aria-hidden="true">
            <circle cx="20" cy="20" r="19" fill="var(--white)"/>
            <path d="M13 10 l4 0 l2 6 l-3 2 c1.5 3 3.5 5 6 6 l2 -3 l6 2 l0 4 c0 1.5 -1 2.5 -2.5 2.5 C18 29.5 10.5 22 10.5 12.5 C10.5 11 11.5 10 13 10 Z" fill="var(--blue-deep)"/>
          </svg>
          <span>555 01 2345</span>
        </div>
      </div>
      <div class="hero-art" role="img" aria-label="Ilustración de un cohete naranja despegando con una explosión de humo naranja desde la pantalla de un portátil"></div>
    </div>
    <div class="headline-band">
      <span class="headline-main">1000 MEGAS + 100GIGAS</span>
      <span class="headline-sub">MOVIL CON LLAMADAS ILIMITADAS</span>
    </div>
  </div>
</body>
</html>
```